New banner design for mortgage broker

Looking for a banner design for mortgage broking company.
- need to use logo
- need to use colours from the logo
- like to use the headshot somehow.
- use slogan ' Helping to navigate your finance journey'
- include listing our services. Home Loans, Investment Loans, First Home Buyers, Self-employed Specialist, Car loans, Past Credit issues.
- call to action to get in contact today on 1300 642 917 or www.harbourvf.com.au
- Banner size 2.4m x 0.6m

```html
<!DOCTYPE html>
<html lang="en">
<head>
<meta charset="utf-8">
<title>Harbour Vale Finance – Banner</title>
<link rel="stylesheet" href="https://fonts.googleapis.com/css2?family=Montserrat:wght@500;600;700;800&display=swap">
<style>
  :root {
    --teal: #1a4f5f;
    --navy: #222238;
    --white: #ffffff;
    --brand-purple: #55308f;
    --portrait-light: #c9a583;
    --portrait-dark: #1f2b4d;
  }
  html, body {
    margin: 0;
    padding: 0;
    width: 1200px;
    height: 300px;
    overflow: hidden;
    background: var(--teal);
  }
  .banner {
    display: block;
    width: 1200px;
    height: 300px;
    font-family: "Montserrat", sans-serif;
  }
  .bg { fill: var(--teal); }
  .contact-band { fill: var(--navy); }
  .headline { fill: var(--white); font-weight: 800; }
  .subheadline { fill: var(--white); font-weight: 700; }
  .services-pill { fill: var(--navy); }
  .services-label { fill: var(--white); font-weight: 700; letter-spacing: 0.5px; }
  .service-list { fill: var(--white); font-weight: 600; }
  .service-dot { fill: var(--white); }
  .logo-pill { fill: var(--white); }
  .brand-name { fill: var(--brand-purple); font-weight: 600; }
  .contact-text { fill: var(--white); font-weight: 500; }
  .icon-stroke { fill: none; stroke: var(--white); stroke-width: 1.4; }
</style>
</head>
<body>
<svg class="banner" viewBox="0 0 1200 300" xmlns="http://www.w3.org/2000/svg">
  <defs>
    <linearGradient id="portraitTone" x1="0" y1="0" x2="0" y2="1">
      <stop offset="0" stop-color="var(--portrait-light)"/>
      <stop offset="0.5" stop-color="#b48a6c"/>
      <stop offset="1" stop-color="var(--portrait-dark)"/>
    </linearGradient>
  </defs>

  <rect class="bg" x="0" y="0" width="1200" height="300"/>
  <rect class="contact-band" x="0" y="254" width="1200" height="46"/>

  <rect x="0" y="0" width="247" height="300" fill="url(#portraitTone)" role="img" aria-label="Headshot of the mortgage broker, smiling, in a navy blazer"/>

  <text class="headline" x="175" y="79" font-size="72" textLength="771" lengthAdjust="spacingAndGlyphs">HELPING TO NAVIGATE</text>
  <text class="subheadline" x="278" y="132" font-size="48" textLength="554" lengthAdjust="spacingAndGlyphs">YOUR FINANCE JOURNEY</text>

  <rect class="services-pill" x="476" y="146" width="217" height="32" rx="16"/>
  <text class="services-label" x="495" y="171" font-size="25" textLength="180" lengthAdjust="spacingAndGlyphs">OUR SERVICES</text>

  <g class="service-list" font-size="28">
    <text x="252" y="210" textLength="178" lengthAdjust="spacingAndGlyphs">HOME LOANS</text>
    <circle class="service-dot" cx="437" cy="205" r="5"/>
    <text x="446" y="210" textLength="268" lengthAdjust="spacingAndGlyphs">INVESTMENT LOANS</text>
    <circle class="service-dot" cx="721" cy="205" r="5"/>
    <text x="731" y="210" textLength="279" lengthAdjust="spacingAndGlyphs">FIRST HOME BUYERS</text>
    <circle class="service-dot" cx="1017" cy="205" r="5"/>

    <text x="252" y="239" textLength="375" lengthAdjust="spacingAndGlyphs">SELF-EMPLOYED SPECIALIST</text>
    <circle class="service-dot" cx="632" cy="234" r="5"/>
    <text x="642" y="239" textLength="155" lengthAdjust="spacingAndGlyphs">CAR LOANS</text>
    <circle class="service-dot" cx="804" cy="234" r="5"/>
    <text x="814" y="239" textLength="275" lengthAdjust="spacingAndGlyphs">PAST CREDIT ISSUES</text>
  </g>

  <rect class="logo-pill" x="976" y="28" width="196" height="68" rx="34"/>
  <text class="brand-name" x="1074" y="64" font-size="28" text-anchor="middle" textLength="150" lengthAdjust="spacingAndGlyphs">HARBOUR</text>
  <text class="brand-name" x="1074" y="82" font-size="10" text-anchor="middle" letter-spacing="2">Vale Finance</text>

  <text class="contact-text" x="336" y="282" font-size="21" textLength="197" lengthAdjust="spacingAndGlyphs">Get in contact today</text>

  <g class="phone-icon">
    <circle class="icon-stroke" cx="578.5" cy="277" r="11"/>
    <path fill="var(--white)" d="M573.5 270.5c1-.8 2-.6 2.6.4l1.3 2.2c.4.8.2 1.6-.5 2.1l-.8.6c.6 1.6 1.8 3.2 3.4 4.3l.8-.6c.7-.5 1.5-.4 2.1.2l1.7 1.8c.7.8.6 1.9-.3 2.6-1.4 1.1-3.4 1.1-5.4-.2-3.4-2.2-5.8-5.8-6.3-9.2-.2-1.7.3-3.2 1.4-4.2z"/>
  </g>
  <text class="contact-text" x="596" y="285" font-size="24" textLength="140" lengthAdjust="spacingAndGlyphs">1300 642 917</text>

  <g class="globe-icon">
    <circle class="icon-stroke" cx="775" cy="278" r="9.5"/>
    <ellipse class="icon-stroke" cx="775" cy="278" rx="4" ry="9.5"/>
    <line class="icon-stroke" x1="765.5" y1="278" x2="784.5" y2="278"/>
    <line class="icon-stroke" x1="767" y1="273" x2="783" y2="273"/>
    <line class="icon-stroke" x1="767" y1="283" x2="783" y2="283"/>
  </g>
  <text class="contact-text" x="792" y="284" font-size="22" textLength="239" lengthAdjust="spacingAndGlyphs">www.harbourvf.com.au</text>
</svg>
</body>
</html>
```